Velvet Shakers business card

We would like a business card designed for our business velvet shakers

We need it to have 2 sides.

More information about the business can be found at www.velvetshakers-example.net

Industry/Entity Type

Business

```html
<!DOCTYPE html>
<html lang="en">
<head>
<meta charset="utf-8">
<title>Velvet Shakers business card</title>
<link rel="stylesheet" href="https://fonts.googleapis.com/css2?family=Ubuntu:wght@400;500;700&family=Lobster&display=swap">
<style>
  :root {
    --backdrop: #e9e6df;
    --card-black: #0d0d0d;
    --card-black-soft: #222;
    --gold: #d8c27e;
    --gold-pale: #e6d7a6;
    --cream: #ece6cf;
    --cream-deep: #cfc7a6;
    --ink: #161616;
  }
  * { box-sizing: border-box; margin: 0; padding: 0; }
  html, body { width: 1200px; height: 885px; overflow: hidden; }
  body {
    background: var(--backdrop);
    font-family: "Ubuntu", Arial, sans-serif;
    position: relative;
  }
  .card {
    position: absolute;
    top: 92px;
    width: 400px;
    height: 700px;
    border-radius: 6px;
    overflow: hidden;
    box-shadow: 0 10px 30px rgba(0,0,0,0.18);
  }
  .card--front {
    left: 160px;
    background: linear-gradient(160deg, var(--card-black-soft) 0%, var(--card-black) 55%);
    color: var(--gold);
    text-align: center;
  }
  .card--back {
    left: 640px;
    background: radial-gradient(ellipse at 45% 40%, #f6f1de 0%, var(--cream) 45%, var(--cream-deep) 100%);
  }
  .brand {
    position: absolute;
    top: 78px;
    left: 0;
    width: 100%;
    display: flex;
    align-items: center;
    justify-content: center;
    gap: 12px;
    font-weight: 700;
    font-size: 40px;
    color: var(--gold);
  }
  .brand__dot {
    width: 16px; height: 16px; border-radius: 50%;
    background: var(--gold);
  }
  .person {
    position: absolute;
    top: 212px;
    width: 100%;
  }
  .person__name {
    font-family: "Lobster", cursive;
    font-size: 40px;
    color: var(--gold);
    line-height: 1;
  }
  .person__role {
    font-size: 24px;
    color: var(--gold-pale);
    margin-top: 4px;
  }
  .contact {
    position: absolute;
    top: 376px;
    width: 100%;
    font-size: 22px;
    line-height: 1.32;
    color: var(--gold);
  }
  .web-band {
    position: absolute;
    left: 0; bottom: 0;
    width: 100%;
    height: 86px;
    background: linear-gradient(180deg, #f3eedb, var(--cream-deep));
    display: flex;
    align-items: center;
    justify-content: center;
    font-size: 22px;
    font-weight: 500;
    color: var(--ink);
  }
  .back-brand {
    position: absolute;
    top: 50%;
    left: 50%;
    transform: translate(-50%, -50%) rotate(90deg);
    display: flex;
    align-items: center;
    gap: 20px;
    white-space: nowrap;
    font-weight: 700;
    font-size: 62px;
    color: var(--ink);
  }
  .back-brand__dot {
    width: 26px; height: 26px; border-radius: 50%;
    background: var(--ink);
  }
</style>
</head>
<body>
  <section class="card card--front" aria-label="Card front">
    <div class="brand"><span class="brand__name">Velvet Shakers</span><span class="brand__dot"></span></div>
    <div class="person">
      <p class="person__name">Marcus</p>
      <p class="person__role">Owner</p>
    </div>
    <div class="contact">
      <p>0400123456</p>
      <p>0400654321</p>
      <p>info@velvetshakers-example.net</p>
      <p>Po Box 1234 Palmhaven</p>
      <p>Coralshire,Australia</p>
    </div>
    <div class="web-band">www.velvetshakers-example.net</div>
  </section>

  <section class="card card--back" aria-label="Card back">
    <div class="back-brand"><span class="back-brand__name">Velvet Shakers</span><span class="back-brand__dot"></span></div>
  </section>
</body>
</html>
```